Still Brook Trail - Business Card

May try various combos of colors from primary & secondary palette attached below. Logo and Catch phrase previous built logo attached should go on front, but change to color palette options noted. may try various color options from minimal to zen like quality/vibe.
On Front: Attached Logo & Phrase
On Back:
https://stillbrooktrail.com/
415.283.7904
stillbrooktrail@openlanterndesk.ai

Contact Information for Business Card

Daniel R. Forsyth, MD Founder & CEO https://stillbrooktrail.com/ 415.283.7904 stillbrooktrail@openlanterndesk.ai

```html
<!DOCTYPE html>
<html lang="en">
<head>
<meta charset="utf-8">
<title>Still Brook Trail – Business Card</title>
<link rel="stylesheet" href="https://fonts.googleapis.com/css2?family=Gilda+Display&family=Montserrat:wght@400;500&family=Alex+Brush&family=Lato:wght@400&display=swap">
<style>
  :root {
    --backdrop: #f3e4e8;
    --terracotta: #b8652a;
    --sand: #e9c6a3;
    --wine: #7d2a1f;
    --ink: #3a2a24;
    --paper: #ffffff;
  }
  * { box-sizing: border-box; margin: 0; padding: 0; }
  html, body { width: 1200px; height: 975px; overflow: hidden; }
  body { background: var(--backdrop); position: relative; }

  .card {
    position: absolute;
    border-radius: 8px;
    box-shadow: 0 6px 18px rgba(120, 70, 60, 0.18);
    overflow: hidden;
  }

  /* Front */
  .card-front {
    left: 90px; top: 110px; width: 600px; height: 350px;
    background: var(--terracotta);
    display: flex; flex-direction: column; align-items: center; justify-content: center;
  }
  .brand-badge {
    width: 74px; height: 74px; border-radius: 50%;
    border: 2px solid var(--paper);
    margin-bottom: 14px;
  }
  .brand-name {
    font-family: "Gilda Display", serif;
    font-weight: 400;
    color: var(--paper);
    font-size: 46px;
    letter-spacing: 0.5px;
    line-height: 1.1;
  }
  .brand-tagline {
    font-family: "Montserrat", sans-serif;
    color: var(--wine);
    font-size: 15px;
    margin-top: 6px;
    letter-spacing: 0.3px;
  }

  /* Back */
  .card-back {
    left: 510px; top: 520px; width: 620px; height: 360px;
    background: var(--sand);
  }
  .back-emblem {
    position: absolute; left: -70px; top: 40px;
    width: 330px; height: 330px;
  }
  .contact-block {
    position: absolute; right: 36px; top: 64px;
    text-align: right;
  }
  .person-name {
    font-family: "Alex Brush", cursive;
    color: var(--terracotta);
    font-size: 56px;
    line-height: 1;
  }
  .person-title {
    font-family: "Montserrat", sans-serif;
    color: var(--wine);
    font-size: 18px;
    margin: 4px 0 18px;
  }
  .contact-list { list-style: none; }
  .contact-item {
    font-family: "Lato", sans-serif;
    color: var(--ink);
    font-size: 16px;
    line-height: 27px;
    display: flex; align-items: center; justify-content: flex-end; gap: 8px;
  }
  .contact-icon { width: 14px; height: 14px; flex: none; }
</style>
</head>
<body>

  <section class="card card-front" aria-label="Business card front">
    <div class="brand-badge" aria-hidden="true"></div>
    <h1 class="brand-name">Still Brook Trail</h1>
    <p class="brand-tagline">Nurturing Calm Minds, Bodies &amp; Hearts</p>
  </section>

  <section class="card card-back" aria-label="Business card back">
    <svg class="back-emblem" viewBox="0 0 330 330" role="img" aria-label="Large brand emblem area">
      <circle cx="165" cy="165" r="150" fill="none" stroke="var(--terracotta)" stroke-width="3"/>
    </svg>

    <div class="contact-block">
      <p class="person-name">Daniel Forsyth</p>
      <p class="person-title">Founder &amp; CEO</p>
      <ul class="contact-list">
        <li class="contact-item">415.283.7904
          <svg class="contact-icon" viewBox="0 0 14 14" aria-hidden="true">
            <circle cx="7" cy="7" r="7" fill="var(--wine)"/>
            <path d="M4.3 3.6 L5.6 3.4 L6.2 5 L5.4 5.7 Q6.2 7.6 8.2 8.6 L8.9 7.8 L10.5 8.4 L10.3 9.7 Q6.6 10.2 4.3 3.6Z" fill="var(--sand)"/>
          </svg>
        </li>
        <li class="contact-item">stillbrooktrail@openlanterndesk.ai
          <svg class="contact-icon" viewBox="0 0 14 14" aria-hidden="true">
            <circle cx="7" cy="7" r="7" fill="var(--wine)"/>
            <rect x="3.5" y="4.5" width="7" height="5" fill="none" stroke="var(--sand)" stroke-width="1"/>
            <path d="M3.5 4.5 L7 7.3 L10.5 4.5" fill="none" stroke="var(--sand)" stroke-width="1"/>
          </svg>
        </li>
        <li class="contact-item">https://stillbrooktrail.com
          <svg class="contact-icon" viewBox="0 0 14 14" aria-hidden="true">
            <circle cx="7" cy="7" r="7" fill="var(--wine)"/>
            <circle cx="7" cy="7" r="3.6" fill="none" stroke="var(--sand)" stroke-width="0.9"/>
            <ellipse cx="7" cy="7" rx="1.5" ry="3.6" fill="none" stroke="var(--sand)" stroke-width="0.9"/>
            <line x1="3.4" y1="7" x2="10.6" y2="7" stroke="var(--sand)" stroke-width="0.9"/>
          </svg>
        </li>
      </ul>
    </div>
  </section>

</body>
</html>
```